依頼詳細
「北辰年金事務研究連盟」の概要・活動内容等を紹介するパンフレットの作成です。パンフレットとはいえ、A4裏表の簡易版でOKです(ページ数2ページ)。全体として、固い厳粛なイメージが出ればよいかと思います。記載する文章等は添付ファイルのとおりですので、配置や色、デザイン等の作成をお願いします。アレンジはお任せします。
記載項目
北辰年金事務研究連盟/ごあいさつ/協議会概要/活動内容(原則、添付ファイルの通り)
サイズ
A4
ページ数
両面
希望イメージ
シンプル 複雑
単色 カラフル
暗い 明るい
日常 高級
遊び心 厳粛
未来的 伝統的
女性的 男性的
希望する色
青系、茶系、グレー系、全体のバランスがよければ必ずしも上記に拘らないです。
納品ファイル
• PNG形式 (.png)
補足説明
協議会のWEBサイトは以下です。
http://hokushin-renmei.net/
内容やイメージの参考にしてください。

やや硬いイメージを保ちつつ、シンプルで分かりやすいという点を判断基準として、選択いたしました。ありがとうございます。

この度は、多くのランサーの方からご提案いただき、大変ありがとうございます。改めて感謝申し上げます。
途中、修正依頼させていただいた方におかれましては、実際の選択ポイントからずれた内容で依頼してしまったこともあり、この点、お詫び申し上げます。(私以外の担当の意見も反映したことによるものです。何卒ご容赦ください。)
今後また案件が発生した際には、ご協力いただければ幸いです。
どうぞ宜しくお願いします。

```html
<!DOCTYPE html>
<html lang="ja">
<head>
<meta charset="utf-8">
<title>北辰年金事務研究連盟 活動内容・協議会概要</title>
<link href="https://fonts.googleapis.com/css2?family=Noto+Sans+JP:wght@400;500;700&display=swap" rel="stylesheet">
<style>
  :root {
    --paper: #fbfaf7;
    --ink: #3a3632;
    --ink-soft: #5a544e;
    --brown-dark: #5e3419;
    --brown-mid: #8a5630;
    --brown-light: #b98a62;
    --table-line: #cfc8bf;
    --table-head: #e6e1da;
    --table-body: #f7f5f1;
    --photo-a: #f4f2ec;
    --photo-b: #dfe3d6;
    --photo-c: #c9cfbe;
  }
  * { margin: 0; padding: 0; box-sizing: border-box; }
  html, body { width: 846px; height: 1200px; overflow: hidden; }
  body {
    background: var(--paper);
    font-family: "Noto Sans JP", sans-serif;
    color: var(--ink);
    position: relative;
  }
  .hero-photo {
    position: absolute; left: 380px; top: 20px; width: 466px; height: 330px;
    background: radial-gradient(ellipse at 62% 50%, var(--photo-c) 0%, var(--photo-b) 35%, var(--photo-a) 62%, rgba(251,250,247,0) 80%);
  }
  .section-title {
    position: absolute; left: 26px;
    font-size: 25px; font-weight: 700; letter-spacing: 1px; color: var(--ink);
  }
  .activity-band {
    position: absolute; left: 26px; height: 40px;
    background: linear-gradient(90deg, var(--brown-dark) 0%, var(--brown-mid) 70%, var(--brown-light) 100%);
    color: #fff; font-size: 20px; font-weight: 700; letter-spacing: 1px;
    display: flex; align-items: center; padding-left: 20px;
  }
  .activity-text {
    position: absolute; left: 40px;
    font-size: 18.5px; line-height: 30px; color: var(--ink-soft);
  }
  .activity-text .indent { padding-left: 170px; }
  .activity-text .gap { margin-top: 14px; }
  .overview-table {
    position: absolute; left: 26px; top: 772px; width: 794px;
    border-collapse: collapse; font-size: 10.5px; line-height: 16px; color: var(--ink-soft);
  }
  .overview-table th, .overview-table td {
    border: 1px solid var(--table-line); padding: 8px 10px; text-align: left; vertical-align: middle;
  }
  .overview-table th { width: 150px; background: var(--table-head); font-weight: 500; text-align: center; }
  .overview-table td { background: var(--table-body); }
  .page-number {
    position: absolute; right: 22px; bottom: 22px; width: 28px; height: 20px;
    background: var(--brown-mid); color: #fff; font-size: 11px; font-weight: 700;
    display: flex; align-items: center; justify-content: center;
  }
</style>
</head>
<body>
  <div class="hero-photo" role="img" aria-label="手のひらで若葉を包み込むやわらかな写真"></div>

  <h2 class="section-title" style="top:36px;">■活動内容</h2>

  <div class="activity-band" style="top:96px; width:530px;">1）社会保険加入促進の啓蒙活動</div>
  <div class="activity-text" style="top:150px;">
    <p>協議会所属の開業社会保険労務士による</p>
    <p class="indent">セミナーの開催（自主開催）</p>
    <p>業界団体様向けのセミナー・勉強会の開催</p>
    <p>その他適正な情報の提供活動</p>
  </div>

  <div class="activity-band" style="top:352px; width:560px;">2）社会保険調査リスク診断のご提供</div>
  <div class="activity-text" style="top:404px;">
    <p>現状の社会保険上の問題点、保険料負担・法的リスクに関する</p>
    <p>診断サービス</p>
  </div>

  <div class="activity-band" style="top:520px; width:610px;">3）社会保険調査対応＆コンサルティング</div>
  <div class="activity-text" style="top:576px;">
    <p>国家資格取得者・社会保険調査対応の専門家として、</p>
    <p>的確な助言・指導の実施</p>
    <p class="gap">各企業様の実情を踏まえた、コンサルティングサービスのご提供</p>
  </div>

  <h2 class="section-title" style="top:730px;">■協議会概要</h2>

  <table class="overview-table">
    <tr><th>法人名</th><td>北辰年金事務研究連盟</td></tr>
    <tr><th>目的</th><td>社会保険の適正な加入を推進し、事業主及び従業員の皆様が安心して働ける環境づくりに寄与すること。<br>加入実態の調査と情報提供を通じ、社会保険制度の健全な運営と発展に貢献する。<br>全国の社会保険労務士の連携を図る。</td></tr>
    <tr><th>代表</th><td>社会保険労務士 山科 隆之（山科労務事務所）</td></tr>
    <tr><th>副代表</th><td>社会保険労務士 白石 恵美（白石人事労務オフィス）</td></tr>
    <tr><th>特別アドバイザー</th><td>元 年金事務所 調査担当官 川端 正道</td></tr>
    <tr><th>設立</th><td>2015年</td></tr>
    <tr><th>所属社会保険労務士数</th><td>48名（2015年9月現在）</td></tr>
    <tr><th>事務局</th><td>〒150-0000 東京都渋谷区桜丘町9-9 北辰ビル5F<br>北辰年金事務研究連盟 事務局<br>http://hokushin-renmei.net/</td></tr>
    <tr><th>TEL</th><td>03-0000-1234（受付 10:00〜17:00）</td></tr>
    <tr><th>FAX</th><td>03-0000-5678</td></tr>
  </table>

  <div class="page-number">02</div>
</body>
</html>
```